Corporate Business Card Design Project

..Hi designers!
I have established a consultancy within strategic communnications, for which I need a business card design - I've seen some of the things you do in here, and they're great! I'll provide some information in the following:
Name: BrookLedger
Tagline: Guiding Dialogue
Service: Strategic communications consulting (primariy internal communication and optimizing): various organisations - e.g. SMEs, NGOs and NPOs - are offered an analysis of their current efforts and, on the basis of that, management consulting tailored their unique challenges and needs.
It's a sole proprietorship - for now! - but it's my plan to employ 5-20 persons over the years. Therefore the card should NOT symbolize a start-up, but communicate a well-established, serious consultancy. Hence, it should also apply to serious companies and organizations - think Veltro or Harwick Pellman Group (both as sender and receiver) ;)
The design should accordingly have a formal, conservative, stylish, corporate, clean look! and ditto colors, eg. black, grey, white etc - corresponding to the logo. The only colour that can appear is the same orange contrast as in my logo (see attachement). Not too bold or dramatic fonds or letters.
I choose the double sided as I think it gives the most professional look: One side with name, titel, phone, e-mail - then a little space - and four additional lines for address.
This composition is if all information should be in the same "column" - feel free to provide suggestions with the address places elsewhere on the one side.
On the other side, I'm only thinkin' something with the logo.
I'd be happy to see different ideas re. the use of the orange contrast, placement of logo, etc.
I do not plan on changing the design of businees cards ever - as I think it is more serious keeping a concept and avoid rebranding - and I'm sure that you can deliver an ever-lasting logo for my company! Thanks :).
Let's play the rest by ear in the correspondance.
Executive level: CEOs, HR directors, communication managers/directors, business owners.
Management Consulting

```html
<!DOCTYPE html>
<html lang="en">
<head>
<meta charset="utf-8">
<title>BrookLedger Business Card</title>
<link href="https://fonts.googleapis.com/css2?family=Gelasio:wght@400&family=Tinos:wght@400&display=swap" rel="stylesheet">
<style>
  :root {
    --canvas: #e6e2dc;
    --card: #050505;
    --white: #f4f4f4;
    --grey: #9a9a9a;
    --icon: #5a5a5a;
    --orange: #f7941d;
    --rule: #8a5a2b;
  }
  * { margin: 0; padding: 0; box-sizing: border-box; }
  html, body {
    width: 1200px; height: 1000px; overflow: hidden;
    background: var(--canvas);
  }
  .canvas { position: relative; width: 1200px; height: 1000px; }
  .card {
    position: absolute;
    width: 687px; height: 392px;
    background: var(--card);
    box-shadow: 0 4px 14px rgba(0,0,0,0.25);
  }
  .card--front { left: 130px; top: 87px; }
  .card--back { left: 377px; top: 510px; }

  .brand { position: absolute; text-align: left; }
  .brand__name {
    font-family: "Gelasio", Georgia, serif;
    font-weight: 400;
    color: var(--white);
    line-height: 1;
    white-space: nowrap;
  }
  .brand__tagline {
    font-family: "Tinos", "Times New Roman", serif;
    color: var(--grey);
    letter-spacing: 2.4px;
    white-space: nowrap;
    text-align: right;
  }
  .card--front .brand { left: 156px; top: 166px; }
  .card--front .brand__name { font-size: 54px; }
  .card--front .brand__tagline { font-size: 11px; margin-top: 2px; }

  .card--back .brand { left: 431px; top: 169px; }
  .card--back .brand__name { font-size: 28px; }
  .card--back .brand__tagline { font-size: 7px; letter-spacing: 1.6px; margin-top: 1px; }

  .divider {
    position: absolute; left: 371px; top: 64px;
    width: 1px; height: 266px; background: var(--rule);
  }
  .person { position: absolute; left: 91px; top: 78px; font-family: "Tinos", "Times New Roman", serif; }
  .person__name { font-family: "Gelasio", Georgia, serif; font-size: 23px; color: var(--white); line-height: 30px; }
  .person__title { font-family: "Gelasio", Georgia, serif; font-size: 21px; color: var(--orange); line-height: 30px; }

  .contact { position: absolute; left: 52px; top: 173px; list-style: none; font-family: "Tinos", "Times New Roman", serif; color: var(--white); font-size: 20px; }
  .contact__item { display: flex; align-items: flex-start; line-height: 26px; margin-bottom: 4px; }
  .contact__item--address { margin-top: 6px; }
  .contact__icon { width: 24px; height: 24px; margin-right: 15px; flex: none; margin-top: 1px; }
  .contact__icon path, .contact__icon rect { fill: var(--icon); }
</style>
</head>
<body>
<main class="canvas">
  <section class="card card--front" aria-label="Business card front">
    <div class="brand">
      <div class="brand__name">BrookLedger</div>
      <div class="brand__tagline">Guiding Dialogue</div>
    </div>
  </section>

  <section class="card card--back" aria-label="Business card back">
    <div class="person">
      <div class="person__name">Daniel Hart</div>
      <div class="person__title">CEO</div>
    </div>
    <ul class="contact">
      <li class="contact__item">
        <svg class="contact__icon" viewBox="0 0 24 24" aria-hidden="true"><path d="M6.5 2.5l3 4-2 2.2c1 2.6 3.2 5 5.8 6.3l2.1-2 4 3-1.6 3.3c-.5.9-1.6 1.3-2.6 1C9.7 18.6 5.4 14.3 3.7 8.8c-.3-1 .1-2.1 1-2.6z"/></svg>
        <span>(44) 0198 765 432</span>
      </li>
      <li class="contact__item">
        <svg class="contact__icon" viewBox="0 0 24 24" aria-hidden="true"><path d="M1 6h22v13H1z M2.5 7.2 12 14l9.5-6.8" fill-rule="evenodd"/><path d="M1 6l11 8 11-8v1.4L12 15.4 1 7.4z" fill="#050505"/></svg>
        <span>dhart@brookledger.com</span>
      </li>
      <li class="contact__item contact__item--address">
        <svg class="contact__icon" viewBox="0 0 24 24" aria-hidden="true"><path d="M12 1.5a7 7 0 0 0-7 7c0 5 7 14 7 14s7-9 7-14a7 7 0 0 0-7-7zm0 10a3 3 0 1 1 0-6 3 3 0 0 1 0 6z" fill-rule="evenodd"/></svg>
        <span>27 Sample Lane<br>Eastbrook<br>USA</span>
      </li>
    </ul>
    <div class="divider"></div>
    <div class="brand">
      <div class="brand__name">BrookLedger</div>
      <div class="brand__tagline">Guiding Dialogue</div>
    </div>
  </section>
</main>
</body>
</html>
```